KIT & BO’S FAREWELL TO GNAT BITES

I require an attractive appealing label with the dimensions 7.5m x 3.5cm
This is a Natural sandfly insect repellent cream formulated by 2 pharmacists Carla Penrose and Tom Whitcombe. It is required for labelling a 50 g jar

Contains Essential Oils of cedar wood, rosemary, cinnamon, citronella, lavender, eucalyptus and clove in a moisturising base.

We would like to see designs using the colour bright duck egg blue as the main colour with dark brown tones for the patterns. An eye catching label is output aim . However any colour combination that is attractive to the eye is welcome
A gloss finish is preferable.
Updates

More designs please

Target Market(s)

Trekkers, outdoor active people, pharmacy, health shops

Colors
abd037
34a6d7
0456a4
33b8a4

Requirements
Must have
• Kit and Bo’s
• Farewell to Gnat bites
• Natural Sandfly Repellent
• Contains Essential Oils of cedar wood, rosemary, cinnamon, citronella, lavender, eucalyptus and clove in a moisturising base.
• Formulated by Australian Pharmacists Carla Penrose and Tom Whitcombe
• Made in Australia
• 0462735190
Nice to have
• Sandfly/ flies
• I have attached a label I use for my mozzie cream and would like a similar font please

```html
<!DOCTYPE html>
<html lang="en">
<head>
<meta charset="utf-8">
<title>Kit &amp; Bo’s Farewell to Gnat Bites – Jar Label</title>
<link rel="stylesheet" href="https://fonts.googleapis.com/css2?family=Quicksand:wght@400;500;700&family=Caveat:wght@500&display=swap">
<style>
  :root {
    --page: #ffffff;
    --sage: #7fa393;
    --mint: #b0dccb;
    --mint-pattern: #a3d1bf;
    --mint-soft: #c7eadc;
    --white: #ffffff;
  }
  * { box-sizing: border-box; margin: 0; padding: 0; }
  html, body { width: 1200px; height: 1200px; overflow: hidden; background: var(--page); }
  .canvas { position: relative; width: 1200px; height: 1200px; }

  .label {
    position: absolute; left: 67px; top: 352px;
    width: 1066px; height: 496px;
    background: var(--sage); overflow: hidden;
    font-family: "Quicksand", sans-serif;
  }
  .label-art { position: absolute; inset: 0; }

  .ingredients {
    position: absolute; left: 26px; top: 78px; width: 200px;
    color: var(--mint-soft); font-size: 22px; line-height: 25px;
    letter-spacing: 0.5px;
  }
  .ingredients-title { color: var(--white); font-weight: 700; font-size: 21px; margin-bottom: 4px; }

  .credits {
    position: absolute; right: 21px; top: 106px; width: 200px;
    text-align: right; color: var(--mint-soft);
    font-size: 22px; line-height: 25px; letter-spacing: 0.5px;
  }
  .credits .name { color: var(--white); }
  .origin { margin-top: 42px; font-size: 24px; line-height: 30px; }

  .product-name {
    position: absolute; left: 333px; top: 192px; width: 400px; height: 112px;
    display: flex; align-items: center; justify-content: center;
    text-align: center; color: var(--white);
    font-size: 30px; font-weight: 500; line-height: 38px; letter-spacing: 0.5px;
  }

  .badge-text {
    position: absolute; left: 500px; top: 422px; width: 112px;
    font-family: "Caveat", cursive; font-size: 17px; line-height: 18px;
    color: var(--mint-soft); text-align: center;
  }
</style>
</head>
<body>
<div class="canvas">
  <section class="label">
    <svg class="label-art" width="1066" height="496" viewBox="0 0 1066 496">
      <circle cx="533" cy="248" r="328" fill="var(--mint)"/>
      <circle cx="533" cy="248" r="328" fill="var(--mint-pattern)" opacity="0.35" role="img" aria-label="Faint hand-drawn leaf and sprig pattern"/>
      <rect x="205" y="182" width="656" height="8" fill="var(--mint-soft)"/>
      <rect x="205" y="192" width="656" height="112" fill="var(--sage)"/>
      <rect x="205" y="306" width="656" height="8" fill="var(--mint-soft)"/>
      <rect x="449" y="414" width="168" height="54" rx="27" fill="var(--sage)"/>
      <circle cx="476" cy="441" r="19" fill="none" stroke="var(--mint)" stroke-width="2"/>
      <line x1="463" y1="454" x2="489" y2="428" stroke="var(--mint)" stroke-width="2"/>
    </svg>

    <div class="ingredients">
      <p class="ingredients-title">Ingredients:</p>
      <p>Contains<br>Essential<br>Oils of cedar<br>wood,<br>rosemary,<br>cinamon,<br>citronella,<br>lavander,<br>eucalyptus<br>and clove in<br>a nourishing<br>base.</p>
    </div>

    <div class="credits">
      <p>Formulated<br>by<br>Australian<br>Pharmacist<br><span class="name">Carla Penrose</span><br>and <span class="name">Tom</span><br><span class="name">Whitcombe</span></p>
      <p class="origin">Made<br>In Australia</p>
    </div>

    <p class="product-name">Kit &amp; Bo’s<br>Farewell to Gnat Bites</p>

    <p class="badge-text">Natural Sandfly<br>Repellent</p>
  </section>
</div>
</body>
</html>
```